Gentle Brook toothpaste tube design

Design a Gentle Brook tube design for our all natural toothpaste. The toothpaste is 100% natural with a smooth marshmallow consistency. It's unique because it's not pastelike at all. The all natural flavors make the toothpaste taste great. The toothpaste is smooth yet still leaves your mouth feeling squeaky clean. We want to market this as an all natural family toothpaste.

The flavor is Mint. (possibly called "Cozy Mint")

We have included our logo (eps & jpg), information that goes on the back of the tube, and the artwork template from the tube supplier for the 4.2oz tube.

We like a vintage earthy retro look and feel but we are not limited to this.

The tubes stand upright as shown in the picture of File 4.
Updates

The finished artwork must include anĀ adobe illustratorĀ file.

Project Deadline Extended

I would like to thank all of the designers for their work on this project. We had a difficult time making a decision since all of the designs were very close to what we expected.

Sincerely,

Wes

Target Market(s)

The target market is families that desire an all natural toothpaste. We will be stressing the 100% natural and great taste.

Requirements
Must have
• Three colors maximum due to tube manufacture restrictions.

Must have "100% natural" and "fluoride free" on front of tube. A reference to the great taste or flavor is also important.

Must say 4.2 oz on the front of the tube, centered, at the bottom.
Nice to have
• Fun, colorful packaging that will stand out. Go to your local store and stand in front of the tootpaste shelves, give us something different!
Should not have
• We do not want a lot of red or blue because these are predominate colors already in use on toothpaste tubes and boxes.

```html
<!DOCTYPE html>
<html lang="en">
<head>
<meta charset="utf-8">
<title>Gentle Brook Toothpaste Tube Artwork</title>
<link href="https://fonts.googleapis.com/css2?family=Arvo:wght@400;700&family=Arimo:wght@400;700&family=Roboto+Condensed:wght@400;700&display=swap" rel="stylesheet">
<style>
  :root {
    --green: #5cb82e;
    --green-dark: #48a51d;
    --green-light: #8fd24f;
    --green-pale: #dcefc6;
    --slate: #3a3d40;
    --orange: #f7941d;
    --ink: #111111;
    --rule: #9a9a9a;
    --box: #dcdcdc;
    --paper: #ffffff;
  }
  * { margin: 0; padding: 0; box-sizing: border-box; }
  html, body { width: 1200px; height: 900px; overflow: hidden; background: var(--paper); }
  body { position: relative; font-family: "Arimo", Arial, sans-serif; }

  .template-frame {
    position: absolute; left: 260px; top: 104px; width: 680px; height: 736px;
    border: 1px solid var(--rule);
  }
  .cut-line {
    position: absolute; left: 260px; width: 680px; height: 6px;
    border-top: 2px dashed var(--ink); border-bottom: 2px dashed var(--ink);
  }
  .cut-line.top { top: 118px; }
  .cut-line.bottom { top: 786px; }

  /* Front panel */
  .front-panel {
    position: absolute; left: 284px; top: 130px; width: 360px; height: 640px;
    background: var(--paper); overflow: hidden; text-align: center;
  }
  .leaf-backdrop {
    position: absolute; left: 0; top: 140px; width: 360px; height: 190px;
    background: radial-gradient(ellipse at 50% 70%, #e4f3d2 0%, #eef8e3 55%, rgba(255,255,255,0) 80%);
  }
  .brand-mark {
    position: absolute; left: 0; right: 0; top: 48px;
    display: flex; align-items: center; justify-content: center; gap: 10px;
  }
  .brand-mark .dot { width: 22px; height: 22px; border-radius: 50%; background: var(--green); }
  .brand-mark .name {
    font-family: "Arvo", Georgia, serif; font-weight: 700; color: var(--green);
    font-size: 40px; line-height: 1;
  }
  .product-name {
    position: absolute; left: 0; right: 0; top: 220px;
    font-family: "Arvo", Georgia, serif; font-weight: 700; color: var(--slate);
    font-size: 40px; letter-spacing: 3px; line-height: 1;
  }
  .product-type {
    position: absolute; left: 0; right: 0; top: 268px;
    font-family: "Arvo", Georgia, serif; color: var(--ink);
    font-size: 22px; letter-spacing: 5px; line-height: 1;
  }
  .grey-strip { position: absolute; left: 0; top: 318px; width: 360px; height: 12px; background: #b9b9b9; }
  .claim-band {
    position: absolute; left: 0; top: 330px; width: 360px; height: 84px;
    background: var(--green-dark); color: var(--paper);
    font-size: 14px; letter-spacing: 1.5px; line-height: 20px; padding-top: 22px;
  }
  .flavor-band {
    position: absolute; left: 0; top: 414px; width: 360px; height: 56px;
    background: var(--green-light); color: var(--paper);
  }
  .flavor-band .flavor-name {
    font-family: "Arvo", Georgia, serif; font-size: 24px; letter-spacing: 1px; line-height: 1; padding-top: 7px;
  }
  .flavor-band .flavor-label { font-size: 15px; letter-spacing: 4px; margin-top: 4px; }
  .info-band {
    position: absolute; left: 0; top: 470px; width: 360px; height: 170px;
    background: linear-gradient(180deg, var(--green-dark) 0%, var(--green) 55%, var(--green-light) 100%);
    color: var(--paper);
  }
  .info-band .natural { position: absolute; left: 0; right: 0; top: 54px; font-size: 14px; font-weight: 700; letter-spacing: 4px; }
  .info-band .tested { position: absolute; left: 0; right: 0; top: 82px; font-family: "Arvo", Georgia, serif; font-weight: 700; font-size: 14px; }
  .info-band .volume { position: absolute; left: 0; right: 0; top: 126px; font-weight: 700; font-size: 15px; letter-spacing: 1px; }
  .new-badge {
    position: absolute; left: 274px; top: 418px; width: 54px; height: 54px; border-radius: 50%;
    background: var(--orange); border: 3px solid var(--paper);
    color: var(--paper); font-weight: 700; font-size: 16px; line-height: 48px;
  }

  /* Back panel */
  .back-panel {
    position: absolute; left: 650px; top: 130px; width: 264px; height: 640px;
    background: var(--paper); text-align: center;
    font-family: "Roboto Condensed", Arial Narrow, sans-serif;
  }
  .back-panel .brand-mark { top: 50px; gap: 7px; }
  .back-panel .brand-mark .dot { width: 14px; height: 14px; }
  .back-panel .brand-mark .name { font-size: 26px; }
  .tagline { position: absolute; left: 0; right: 0; top: 128px; font-weight: 700; font-size: 14px; color: var(--ink); }
  .copy-block {
    position: absolute; left: 16px; right: 16px; top: 156px;
    color: var(--green); font-weight: 700; font-size: 10.5px; line-height: 13px;
  }
  .copy-block p { margin-bottom: 9px; }
  .best-results { position: absolute; left: 0; right: 0; top: 406px; color: var(--ink); font-weight: 700; font-size: 9.5px; line-height: 12px; }
  .code-box { position: absolute; left: 16px; top: 440px; width: 90px; height: 160px; background: var(--box); }
  .contact {
    position: absolute; left: 136px; top: 468px; text-align: left;
    color: var(--green); font-weight: 700; font-size: 10px; line-height: 12px;
  }
  .contact p { margin-bottom: 8px; }
</style>
</head>
<body>
  <div class="template-frame"></div>
  <div class="cut-line top"></div>
  <div class="cut-line bottom"></div>

  <section class="front-panel">
    <div class="leaf-backdrop" role="img" aria-label="Soft pale green leaf pattern backdrop"></div>
    <div class="brand-mark"><span class="dot"></span><span class="name">Gentle Brook</span></div>
    <div class="product-name">NATURAL</div>
    <div class="product-type">TOOTHPASTE</div>
    <div class="grey-strip"></div>
    <div class="claim-band">FLUORIDE-FREE<br>TOOTHPASTE</div>
    <div class="flavor-band">
      <div class="flavor-name">COZY MINT</div>
      <div class="flavor-label">FLAVOR</div>
    </div>
    <div class="info-band">
      <div class="natural">100% NATURAL</div>
      <div class="tested">Family tested &nbsp;|&nbsp; Family approved</div>
      <div class="volume">4.2 FL. OZ.</div>
    </div>
    <div class="new-badge">NEW</div>
  </section>

  <section class="back-panel">
    <div class="brand-mark"><span class="dot"></span><span class="name">Gentle Brook</span></div>
    <div class="tagline">Naturally healthy for your family.</div>
    <div class="copy-block">
      <p>Natural Ingredients: Vegetable glycerin, De-ionized water, Xylitol, Calcium carbonate, USDA organic flavor concentrate, Sodium coco-sulfate (derived from coconut oil), and Carrageenan (extracted from seaweed).</p>
      <p>No parabens, no gluten, no glycols, no SLS, no TEA, no formaldehyde, no artificial flavors, no artificial dye, no artificial sweetener, no dairy, no sorbitol, no saccharine, no peroxides, and no fluoride!</p>
      <p>Directions: Adults and children 2 years of age and older brush teeth thoroughly, preferably after each meal or at least twice a day or as directed by a dentist.</p>
      <p>Children under 2 years: consult a dentist.</p>
    </div>
    <div class="best-results">FOR BEST RESULTS, SQUEEZE TUBE<br>FROM THE TOP DOWN.</div>
    <div class="code-box"></div>
    <div class="contact">
      <p>Gentle Brook LLC<br>1200 Willow Ln<br>Fairview, MI 48000<br>Made in USA</p>
      <p>Questions?<br>www.gentlebrook.com<br>info@gentlebrook.com</p>
      <p>© 2011 Gentle Brook LLC</p>
    </div>
  </section>
</body>
</html>
```